Web Design Project (Renewable Energy Services Company)

Hello crowd,

We are looking to create a website for a new company. We would like to have the page already coded, if you do not provide the code as well, please indicate so. I am including a very preliminary approximation of the wireframe.

We do not have the logo either the color pallet, however we have in mind couple websites that would be similar tho these.

http://www.brovanta.example/en/

and

http://www.lumidrax.example/

We did an approximated wireframe our our website, not necesarly to decide on the layout but rather to know how many pages will be needed. It would be around 10 pages. We will need a section that will be an e-commerce page to sell products such as engineering instrumentation, software and consumables such as cable and connectors.

Our company will be called TORVO. We will be based in Monterrey, Mexico. Our focused will be the development of renewable energy projects. Similar scope of services than http://www.brovanta.example/en/ but only for wind and solar projects.

We like something minimalistic. Some of the things that the logo might or might not include would be the monterrey famous hill, but not strictly necessary.
http://en.wikinota.example/wiki/Cerro_de_la_Silla

also TORVO (which stands for TOrnados RVOlenta) the name is similar the bird (seagal) or wind turbines and sun...any of these are only suggestions and we are open to receive any proposals.

There must be a
home page
services page (some subsections)
products page (some subsections)
contact page with contact form

and some additional subsections like careers and partnerships.

We are very excited to start hearing about this project.
Updates

Please for the logo, do not restrict your ideas to the ones provided as it has generated too specific logos. Pleae just allow your imagination to flow for a company that develops renewable energy projects.

Target Market(s)

large companies interested in developing renewable energy projects

Industry/Entity Type

E-Commerce

Requirements
Must have
• Minimalistic and unique design.
Nice to have
• contact form to save contacts in a database

Should not have
• We are looking a very minimalistic logo. It should not be an explicit wind turbine a seagal or anything like that. we are looking for abstract, simple and minimalistic image.

```html
<!DOCTYPE html>
<html lang="en">
<head>
<meta charset="utf-8">
<title>TORVO – Renewable Energy Projects</title>
<link rel="stylesheet" href="https://fonts.googleapis.com/css2?family=PT+Sans+Narrow:wght@400;700&family=PT+Sans:wght@700&display=swap">
<style>
:root{
  --navy:#0d2a4f;
  --brand:#1a5fb4;
  --nav:#2f4a6a;
  --accent:#7ab51d;
  --band:#eeeff3;
  --frame:#9ab4f0;
  --teal-dark:#145f6a;
  --teal:#1c8c8e;
  --ocean:#145c8f;
  --caption:rgba(38,38,96,.78);
  --pill:#c9c3a0;
  --title:#1a56a0;
  --body:#3a3f4a;
  --events:#eeebea;
  --link:#2a78d6;
  --tab:#c4ccd4;
  --footer:#1e1e1e;
  --footer-link:#4f6f9a;
  --footer-text:#8aa0bf;
}
*{margin:0;padding:0;box-sizing:border-box}
html,body{width:1118px;height:1200px;overflow:hidden;background:#fff}
body{font-family:"PT Sans Narrow",Arial Narrow,sans-serif;color:var(--body)}
.page{position:absolute;left:0;top:0;width:1024px;height:1099px;transform:scale(1.0918);transform-origin:0 0}
.abs{position:absolute}
.topbar{left:0;top:0;width:1024px;height:26px;background:var(--navy);font-family:"PT Sans",sans-serif;font-size:12px;letter-spacing:1px;color:#d8e2f0}
.topbar span{position:absolute;top:6px}
.logo{left:68px;top:38px;display:flex;align-items:center;gap:14px}
.logo-mark{width:74px;height:74px;border-radius:50%;background:var(--brand)}
.logo-name{font-size:46px;color:var(--brand);letter-spacing:3px;font-weight:400}
.nav a{position:absolute;top:72px;font-family:"PT Sans",sans-serif;font-size:15px;letter-spacing:1.5px;color:var(--nav);text-decoration:none}
.nav .current{border-bottom:3px solid var(--accent);padding:0 15px 2px}
.band{left:0;top:186px;width:1024px;height:339px;background:var(--band);border-top:2px solid #c9cbd2;border-bottom:2px solid #c9cbd2}
.slider{left:71px;top:142px;width:888px;height:426px;border:4px solid var(--frame);background:linear-gradient(#7ea6d8 0%,#b9cfe6 30%,#5d7a4c 55%,#3f5a36 80%,#8a8f80 100%)}
.caption{left:627px;top:386px;width:332px;height:158px;background:var(--caption);color:#fff}
.caption .pill{position:absolute;left:4px;top:4px;width:109px;height:28px;border-radius:6px;background:var(--pill);color:#1f1f2a;font-size:17px;padding:3px 0 0 31px}
.caption p{position:absolute;left:35px;top:42px;width:292px;font-size:12.5px;line-height:23px}
.caption .more{position:absolute;right:20px;top:132px;font-size:17px}
.dots{left:80px;top:543px;display:flex;gap:8px}
.dots i{width:20px;height:20px;border-radius:50%;background:#f3f4fa;border:3px solid #2b2f6a}
.card{top:579px;width:293px;height:158px;border-radius:8px;color:#fff}
.card h3{position:absolute;left:10px;top:5px;width:271px;height:30px;border:1px solid rgba(255,255,255,.55);border-radius:8px;font-weight:400;font-size:19px;padding:2px 0 0 12px}
.card .thumb{position:absolute;left:11px;top:51px;width:112px;height:90px}
.card p{position:absolute;left:135px;top:52px;width:150px;font-family:"PT Sans",sans-serif;font-size:12px;letter-spacing:1px;line-height:18px}
.card .read{position:absolute;right:14px;top:140px;font-family:"PT Sans",sans-serif;font-size:12px;letter-spacing:1px}
.about h2{position:absolute;left:73px;top:756px;font-weight:400;font-size:20px;color:var(--title)}
.about p{position:absolute;left:83px;width:625px;font-size:13px;line-height:23px}
.events{left:729px;top:755px;width:234px;height:220px;background:var(--events);border-radius:8px}
.events h2{position:absolute;left:6px;top:9px;width:242px;height:34px;background:#fff;border-radius:8px;font-weight:400;font-size:20px;color:var(--title);padding:3px 0 0 10px}
.event{position:absolute;left:14px;width:214px;font-size:12.5px;line-height:23px}
.event b{font-weight:400;font-size:18px;color:var(--link)}
.event em{position:absolute;right:-1px;top:4px;font-style:normal;font-size:10.5px;color:#222}
.events hr{position:absolute;left:9px;top:129px;width:213px;border:0;border-top:1px solid var(--title)}
.more-tab{left:963px;top:892px;width:25px;height:77px;background:var(--tab);border-radius:0 6px 6px 0;color:var(--link);font-size:14px;text-align:center;line-height:15px;padding-top:8px}
.footer{left:0;top:1007px;width:1024px;height:92px;background:var(--footer);font-family:"PT Sans",sans-serif;font-size:12px;letter-spacing:1px}
.footer span{position:absolute}
.footer .lnk{color:var(--footer-link);top:19px}
.footer .sm{color:var(--footer-text);top:44px;font-size:11px}
.send{left:665px;top:33px;display:flex;align-items:center;gap:10px;color:#e8e8e8;font-size:13px;letter-spacing:0}
.social{left:838px;top:26px;width:156px;height:39px;background:#262626}
.social i{position:absolute;top:8px;width:24px;height:24px;border-radius:3px}
</style>
</head>
<body>
<div class="page">
  <header>
    <div class="abs topbar"><span style="left:724px">Welcome, Guest</span><span style="left:854px">LOGIN</span><span style="left:910px">REGISTER</span></div>
    <div class="abs logo"><div class="logo-mark"></div><div class="logo-name">TORVO</div></div>
    <nav class="nav">
      <a class="current" href="#" style="left:553px">Home</a>
      <a href="#" style="left:661px">Services</a>
      <a href="#" style="left:764px">Products</a>
      <a href="#" style="left:865px">Contact Us</a>
    </nav>
  </header>

  <div class="abs band"></div>
  <section class="abs slider" role="img" aria-label="Photo of the saddle-shaped mountain rising above the city of Monterrey"></section>
  <div class="abs caption">
    <div class="pill">Heading</div>
    <p>Lorem ipsum dolor sit amet, consectetuer adipiscing elit. Nunc suscipit. Suspendisse enim arcu, convallis non, cursus sed, dignissim et, est. Aenean semper aliquet libero. In ante velit, cursus ut, ultrices vitae, tempor ut, risus. Duis pulvinar.</p>
    <span class="more">More</span>
  </div>
  <div class="abs dots"><i></i><i></i><i></i><i></i></div>

  <section class="abs card" style="left:67px;background:var(--teal-dark)">
    <h3>Engineering Instrumentation</h3>
    <div class="thumb" role="img" aria-label="Wind turbines under a blue sky" style="background:linear-gradient(#3d7fc4,#a9cde8 60%,#c9c25a)"></div>
    <p>Lorem ipsum dolor sit amet, consec tetuer adipiscing elit. Praesent vestibulum molestie lacus.</p>
    <span class="read">Read More</span>
  </section>
  <section class="abs card" style="left:369px;background:var(--teal)">
    <h3>Software and Consumables</h3>
    <div class="thumb" role="img" aria-label="Puzzle pieces with connected computers" style="left:11px;width:117px;background:linear-gradient(#fff,#e4e4e4 60%,#c9c9c9)"></div>
    <p style="left:143px">Lorem ipsum dolor sit amet, consec tetuer adipiscing elit. Praesent vestibulum molestie lacus.</p>
    <span class="read">Read More</span>
  </section>
  <section class="abs card" style="left:671px;background:var(--ocean)">
    <h3>Cable and Connectors</h3>
    <div class="thumb" role="img" aria-label="Cable connectors close-up" style="left:10px;top:49px;width:119px;background:linear-gradient(135deg,#9fc3e6,#e6eef6 50%,#5a86b8)"></div>
    <p style="left:144px;top:50px">Lorem ipsum dolor sit amet, consec tetuer adipiscing elit. Praesent vestibulum molestie lacus.</p>
    <span class="read" style="top:136px">Read More</span>
  </section>

  <section class="about">
    <h2>About Us</h2>
    <p style="top:796px">Lorem ipsum dolor sit amet, consectetuer adipiscing elit. Nunc suscipit. Suspendisse enim arcu, convallis non, cursus sed, dignissim et, est. Aenean semper aliquet libero. In ante velit, cursus ut, ultrices vitae, tempor ut, risus. Duis pulvinar. Lorem ipsum dolor sit amet, consectetuer adipiscing elit. Nunc suscipit. Suspendisse enim arcu, convallis non, cursus sed, dignissim et, est. Aenean semper aliquet libero. In ante velit, cursus ut, ultrices vitae, tempor ut, risus. Duis pulvinar. Lorem ipsum dolor sit amet, consectetuer adipiscing elit. Nunc suscipit. Suspendisse enim arcu, convallis non, cursus sed, dignissim et, est.</p>
    <p style="top:934px">Aenean semper aliquet libero. In ante velit, cursus ut, ultrices vitae, tempor ut, risus. Duis pulvinar. Lorem ipsum dolor sit amet, consectetuer adipiscing elit.</p>
  </section>

  <aside class="abs events">
    <h2>Events</h2>
    <div class="event" style="top:52px"><b>Attending &amp; Speaking</b><em>March 19-21, 2012</em><br>Northwind Energy Finance Summit<br>New York City, New York, USA</div>
    <hr>
    <div class="event" style="top:140px"><b>Attending &amp; Speaking</b><em>March 19-21, 2012</em><br>Northwind Energy Finance Summit<br>New York City, New York, USA</div>
  </aside>
  <div class="abs more-tab">M<br>O<br>R<br>E</div>

  <footer class="abs footer">
    <span class="lnk" style="left:167px">Home</span>
    <span class="lnk" style="left:243px">Services</span>
    <span class="lnk" style="left:328px">Products</span>
    <span class="lnk" style="left:419px">Contact Us</span>
    <span class="sm" style="left:93px">Copyright © 2012 Brovanta, Inc. All Rights Reserved</span>
    <span class="sm" style="left:412px">Terms of Use</span>
    <span class="sm" style="left:514px">Privacy Policy</span>
    <div class="abs send">
      <svg width="28" height="20" viewBox="0 0 28 20"><rect x="1" y="1" width="26" height="18" fill="#d8d8d8" stroke="#999"/><path d="M1 1 L14 11 L27 1" fill="none" stroke="#888" stroke-width="1.5"/></svg>
      <span style="position:static">SEND A MESSAGE</span>
    </div>
    <div class="abs social">
      <i style="left:16px;background:#5ab3e0"></i>
      <i style="left:48px;background:#3b5b9a"></i>
      <i style="left:80px;background:#555"></i>
      <i style="left:112px;background:#f07b1e"></i>
    </div>
  </footer>
</div>
</body>
</html>
```